Wordpress Design Project

We need a Web page. That runs under wordpress. We have a domain- www.lomavrenta.us

The page shall consist of five buttons- home, about, services, projects, contact.

My current clients are-

Bright quarry electronics, inc.
Pelwinter coffee
Vantrocket
Lease a Corner
Grolf
Top penny depot
Quillans Steakhouse
RKVELO

Incorporate customer logos in my website

Our services include:

-Fire alarm systems
-Fire alarm system design

-Security
-Card Access
-CCTV/IP Cameras

-Communication systems
-Intercom/entry phone
-Nurse call systems

The page needs to be simple and professional.

The site needs to be loaded on word press and fully functional.
I also need to have the ability to make small edits later on, or when we add clients to add to the list.
Updates

Target Market(s)

Target market is- electrical contractors, end customers

Industry/Entity Type

Electronics

Requirements
Must have
• Partners-
http://www.structuresolutions.dravenko.com/bt/global/en/firesafety/fire-safety-products/Pages/fire-safety-products.aspx

http://www.dravenko.com/entry/cc/en/
http://www.kolbrisk.com/
http://www.mistyharbor.com/
Plaxtondale
Voribel

```html
<!DOCTYPE html>
<html lang="en">
<head>
<meta charset="utf-8">
<title>Lomav Fire and Security</title>
<link rel="stylesheet" href="https://fonts.googleapis.com/css2?family=Arimo:wght@400;700&family=Open+Sans:wght@600;700;800&display=swap">
<style>
:root{
  --orange:#ff6a00;
  --orange-deep:#e13a06;
  --red:#cc3300;
  --text:#555;
  --dark:#333;
  --btn:#4a4a4a;
  --rule:#cfcfcf;
  --side:#f4f4f4;
}
*{margin:0;padding:0;box-sizing:border-box}
html,body{width:984px;height:1200px;overflow:hidden;background:#fff;font-family:Arimo,Arial,sans-serif;color:var(--text)}
.page{position:relative;width:984px;height:1200px}
.abs{position:absolute}
.topbar{left:0;top:0;width:984px;height:29px;background:var(--orange)}
.toplinks{right:20px;top:8px;font-size:12px;color:#7a1d00}
.toplinks span{margin:0 6px}
.brand{left:22px;top:40px;display:flex;align-items:center;gap:14px}
.brand-mark{width:92px;height:92px;border-radius:50%;background:var(--orange)}
.brand-name{font-family:"Open Sans",sans-serif;font-weight:800;font-size:58px;line-height:56px;color:#444;letter-spacing:-1px}
.brand-tag{font-family:"Open Sans",sans-serif;font-weight:600;font-size:20px;color:#444;line-height:24px}
.call{right:26px;top:57px;font-size:19px;color:#111}
.search{left:719px;top:103px;width:192px;height:27px;background:#ccc;border:1px solid #aaa;font-size:12px;color:#666;padding:7px 15px}
.go{left:914px;top:103px;width:50px;height:27px;background:#555;color:#fff;font-size:12px;text-align:center;line-height:27px}
.nav{left:20px;top:152px;width:944px;height:34px;background:linear-gradient(#3a3a3a,#000);display:flex;box-shadow:0 10px 12px -8px rgba(0,0,0,.35)}
.nav-home{width:68px;height:34px;background:#555;display:flex;align-items:center;justify-content:center;position:relative}
.nav-home:after{content:"";position:absolute;bottom:-6px;left:28px;border:6px solid transparent;border-top-color:#555;border-bottom:0}
.nav a{color:#fff;text-decoration:none;font-size:14px;padding:0 15px;line-height:34px;border-right:1px solid #333}
.nav a:first-of-type{margin-left:13px}
.hero-photo{left:20px;top:210px;width:610px;height:347px;background:radial-gradient(circle at 40% 45%,#e14b3a,#b21a12 55%,#7a0c08)}
.slide{left:630px;width:334px;color:#fff;padding:20px 0 0 39px}
.slide h3{font-weight:400;font-size:22px;text-shadow:1px 1px 2px rgba(0,0,0,.3)}
.slide p{font-size:12px;color:#8a1a00;line-height:18px;margin-top:6px;width:280px}
.s1{top:210px;height:116px;background:linear-gradient(90deg,#ff5a00,#ff8a1e)}
.s2{top:326px;height:116px;background:#e63a08;border-top:1px solid #ff6a2a}
.s3{top:442px;height:115px;background:#e63a08;border-top:1px solid #f25a25}
.pointer{left:604px;top:256px;border:13px solid transparent;border-right-color:#ff5a00;border-left:0}
.sidebar{left:686px;top:557px;width:278px;height:571px;background:linear-gradient(#eee,#fafafa 40%,#fff);border:1px solid #ddd}
h2.title{font-family:"Open Sans",sans-serif;font-weight:700;font-size:18px;color:#555}
h2.title b{color:var(--red)}
.welcome{left:30px;top:580px;font-family:"Open Sans",sans-serif;font-weight:700;font-size:35px;color:var(--red)}
.lead{left:30px;top:641px;font-size:12px;font-weight:700;color:var(--orange)}
.body{left:30px;top:676px;width:636px;font-size:12px;line-height:20px}
.btn{height:31px;background:var(--btn);color:#fff;font-size:12px;line-height:31px;text-align:center;box-shadow:0 1px 2px rgba(0,0,0,.3)}
.rule{height:1px;background:var(--rule)}
.services li{list-style:none;font-size:12px;height:31.5px;display:flex;gap:24px;align-items:flex-start}
.services li svg{margin-top:2px;flex:none}
.about p{font-size:12px;line-height:20px;width:316px;margin-bottom:18px;position:relative}
.about p b{color:var(--orange);margin-left:26px}
.about p:before{content:"";position:absolute;left:4px;top:7px;width:7px;height:7px;border-radius:50%;background:#222}
.logo-name{font-family:Arimo,Arial,sans-serif;font-weight:700;font-size:13px;display:flex;align-items:center;gap:5px;white-space:nowrap}
.logo-name i{width:12px;height:12px;display:inline-block}
.contact{left:687px;top:900px;width:276px;text-align:center;font-size:11px;color:#111;line-height:13px}
.contact .k{color:var(--orange);font-weight:700}
.footer{left:0;top:1128px;width:984px;height:72px;background:var(--dark);color:#fff}
.social{display:flex;gap:4px}
.social i{width:29px;height:29px;border-radius:4px;display:block}
</style>
</head>
<body>
<div class="page">
  <div class="abs topbar"></div>
  <div class="abs toplinks">Sign Up for Email Exclusive<span>|</span>Rewards<span>|</span>Customer Care<span>|</span>Find a Store</div>

  <div class="abs brand">
    <div class="brand-mark"></div>
    <div><div class="brand-name">LOMAV</div><div class="brand-tag">Fire and Security</div></div>
  </div>
  <div class="abs call">Call : 555-0178</div>
  <div class="abs search">Search</div>
  <div class="abs go">Go</div>

  <nav class="abs nav">
    <div class="nav-home"><svg width="18" height="16" viewBox="0 0 18 16"><path d="M9 0 18 8H15V16H11V11H7V16H3V8H0Z" fill="#fff"/></svg></div>
    <a>ABOUT US</a><a>PROJECTS</a><a>CONATCT</a>
  </nav>

  <div class="abs hero-photo" role="img" aria-label="Close-up photo of a red fire alarm box"></div>
  <div class="abs slide s1"><h3>LOREM IPSUM</h3><p>is simply dummy text of the printing and typesetting industry.</p></div>
  <div class="abs slide s2"><h3>LOREM IPSUM</h3><p>is simply dummy text of the printing and typesetting industry.</p></div>
  <div class="abs slide s3"><h3>LOREM IPSUM</h3><p>is simply dummy text of the printing and typesetting industry.</p></div>
  <div class="abs pointer"></div>

  <div class="abs welcome">Welcome !</div>
  <div class="abs lead">Contrary to popular belief, Lorem Ipsum is not simply random text.</div>
  <p class="abs body">It has roots in a piece of classical Latin literature from 45 BC, making it over 2000 years old. Edmund Larkwell, a Latin professor at Harrowfield College in Virginia, looked up one of the more obscure Latin words, consectetur, from a Lorem Ipsum passage, and going through the cites of the word in classical literature, discovered the undoubtable source. Lorem Ipsum comes from sections 1.10.32 and 1.10.33 of "de Finibus Bonorum et Malorum" (The Extremes of Good and Evil) by Varrus, written in 45 BC.</p>
  <div class="abs btn" style="left:577px;top:784px;width:85px">read more</div>
  <div class="abs rule" style="left:40px;top:838px;width:611px"></div>

  <h2 class="abs title" style="left:40px;top:856px"><b>About</b> Us</h2>
  <div class="abs about" style="left:40px;top:893px">
    <p><b>Lorem ipsum dolor sit amet conse</b> ctetur adipisicing elit, sed do eiusmod tempor incididunt ut labore et dolore magna aliqua. Ut enim ad minim veniam, quis nostrud exercitation ullamco laboris nisi ut aliquip.</p>
    <p><b>Lorem ipsum dolor sit amet conse</b> ctetur adipisicing elit, sed do eiusmod tempor incididunt ut labore et dolore magna aliqua. Ut enim ad minim veniam, quis nostrud exercitation ullamco laboris nisi ut aliquip.</p>
  </div>
  <div class="abs btn" style="left:44px;top:1093px;width:86px">read more</div>
  <div class="abs" style="left:374px;top:853px;width:1px;height:273px;background:var(--rule)"></div>

  <h2 class="abs title" style="left:406px;top:864px">Our Partners</h2>
  <div class="abs logo-name" style="left:404px;top:915px;color:#c22;font-size:12px"><i style="background:#c22"></i>Misty Harbor</div>
  <div class="abs" style="left:422px;top:944px;font-size:9px;color:#444">by Plaxtondale</div>
  <div class="abs logo-name" style="left:508px;top:917px;color:#222;font-size:12px">Kolbrisk Resource Site</div>
  <div class="abs logo-name" style="left:534px;top:934px;color:#1a9a9a;font-size:16px">Dravenko</div>
  <div class="abs rule" style="left:402px;top:976px;width:255px"></div>

  <h2 class="abs title" style="left:406px;top:988px">Our Clients</h2>
  <div class="abs logo-name" style="left:406px;top:1046px;color:#1a6b3a"><i style="border-radius:50%;background:#1a6b3a"></i>Pelwinter</div>
  <div class="abs logo-name" style="left:488px;top:1046px;color:#1a3d8f"><i style="background:#f2c200"></i>Vantrocket</div>
  <div class="abs logo-name" style="left:578px;top:1046px;color:#8a3a1a">Quillans</div>
  <div class="abs logo-name" style="left:414px;top:1097px;color:#1a3d8f"><i style="background:#1a3d8f"></i>Lease a Corner</div>
  <div class="abs logo-name" style="left:530px;top:1088px;color:#1a4fa8;font-size:18px">Grolf</div>

  <aside class="abs sidebar"></aside>
  <h2 class="abs title" style="left:710px;top:603px"><b>Our</b> Services</h2>
  <ul class="abs services" style="left:716px;top:648px;color:#555">
    <li><svg width="10" height="8" viewBox="0 0 10 8"><path d="M0 0 4 4 0 8ZM5 0 9 4 5 8Z" fill="#888"/></svg>The standard chunk of Lorem Ipsum</li>
    <li><svg width="10" height="8" viewBox="0 0 10 8"><path d="M0 0 4 4 0 8ZM5 0 9 4 5 8Z" fill="#888"/></svg>The standard chunk of Lorem Ipsum</li>
    <li><svg width="10" height="8" viewBox="0 0 10 8"><path d="M0 0 4 4 0 8ZM5 0 9 4 5 8Z" fill="#888"/></svg>The standard chunk of Lorem Ipsum</li>
    <li><svg width="10" height="8" viewBox="0 0 10 8"><path d="M0 0 4 4 0 8ZM5 0 9 4 5 8Z" fill="#888"/></svg>The standard chunk of Lorem Ipsum</li>
    <li><svg width="10" height="8" viewBox="0 0 10 8"><path d="M0 0 4 4 0 8ZM5 0 9 4 5 8Z" fill="#888"/></svg>The standard chunk of Lorem Ipsum</li>
    <li><svg width="10" height="8" viewBox="0 0 10 8"><path d="M0 0 4 4 0 8ZM5 0 9 4 5 8Z" fill="#888"/></svg>The standard chunk of Lorem Ipsum</li>
  </ul>
  <div class="abs btn" style="left:715px;top:839px;width:86px">read more</div>
  <div class="abs rule" style="left:698px;top:891px;width:254px"></div>
  <div class="abs" style="left:803px;top:913px;width:44px;height:44px;border-radius:50%;background:var(--orange)"></div>
  <div class="abs contact">
    <div style="margin-top:77px;font-family:'Open Sans',sans-serif;font-weight:700;font-size:19px;line-height:22px;color:#333">Dale <span style="color:var(--orange)">Voss</span></div>
    <div style="font-size:12px;margin-bottom:14px">Sales Engineer</div>
    <div>1240 Palmera Ave, Suite B210, Port Ellery, WA 98999</div>
    <div><span class="k">Phone:</span> 600-555-0178 &nbsp;|&nbsp; <span class="k">Fax:</span> 888-555-0192</div>
    <div><span class="k">E-mail:</span> dale@lomavrenta.us</div>
    <div>www.lomavrenta.us</div>
  </div>

  <footer class="abs footer">
    <div class="abs" style="left:389px;top:30px;font-size:12px">2011 © Copyrights.lomavrenta.Reserved</div>
    <div class="abs" style="left:861px;top:16px;font-size:12px">Connect with us:</div>
    <div class="abs social" style="left:849px;top:33px"><i style="background:#3b6fc4"></i><i style="background:#39a8e0"></i><i style="background:#f2901e"></i></div>
  </footer>
</div>
</body>
</html>
```